Harbourlight ceramics Ltd
Stone and tile specialists
Simple
Colin Ashby-Rhodes
Director
Address not needed on the business card
colin@harbourlightceramics.example
www.harbourlightceramics.example
We also require an A4 folder promotional sheet, a letter head, complimentry slip and a van design.
Logo and the web address. All other info on the other side. In UK we say mob: instead of cell.

```html
<!DOCTYPE html>
<html lang="en">
<head>
<meta charset="utf-8">
<title>Harbourlight ceramics Ltd – Business Card</title>
<link rel="stylesheet" href="https://fonts.googleapis.com/css2?family=Open+Sans:ital,wght@0,600;0,700;1,400&family=Tinos&display=swap">
<style>
  :root {
    --backdrop: #2e2e2f;
    --card: #ffffff;
    --brand-grey: #6d6e70;
    --brand-orange: #f26a1b;
    --band-grey: #8c8d8f;
    --text-dark: #2a2a2a;
    --text-muted: #6b6b6b;
  }
  * { margin: 0; padding: 0; box-sizing: border-box; }
  html, body {
    width: 1200px;
    height: 780px;
    overflow: hidden;
    background: var(--backdrop);
  }
  .canvas {
    position: relative;
    width: 1200px;
    height: 780px;
  }
  .card {
    position: absolute;
    left: 150px;
    top: 100px;
    width: 900px;
    height: 580px;
    background: var(--card);
    border-radius: 34px;
    overflow: hidden;
    box-shadow: 0 18px 40px rgba(0, 0, 0, 0.45);
  }
  .brand-watermark {
    position: absolute;
    left: 620px;
    top: 110px;
    width: 180px;
    height: 180px;
    border-radius: 18px;
    background: var(--brand-orange);
    opacity: 0.1;
  }
  .brand {
    position: absolute;
    left: 108px;
    top: 118px;
    display: flex;
    align-items: flex-start;
    gap: 18px;
    font-family: "Open Sans", sans-serif;
    font-weight: 600;
    color: var(--brand-grey);
  }
  .brand-mark {
    width: 34px;
    height: 34px;
    margin-top: 22px;
    background: var(--brand-orange);
  }
  .brand-name {
    display: flex;
    flex-direction: column;
    line-height: 1;
  }
  .brand-name .primary {
    font-size: 72px;
    letter-spacing: -1px;
  }
  .brand-name .secondary {
    margin-top: 8px;
    font-size: 28px;
    letter-spacing: 12px;
    text-transform: uppercase;
  }
  .person {
    position: absolute;
    left: 108px;
    top: 318px;
    font-family: "Open Sans", sans-serif;
  }
  .person-name {
    font-size: 27px;
    font-weight: 700;
    color: var(--brand-orange);
  }
  .person-role {
    font-size: 16px;
    font-style: italic;
    color: var(--text-muted);
    margin-top: 2px;
  }
  .contacts {
    position: absolute;
    left: 108px;
    top: 404px;
    list-style: none;
    font-family: "Tinos", serif;
    font-size: 20px;
    color: var(--text-dark);
  }
  .contacts li {
    display: flex;
    align-items: center;
    gap: 16px;
    height: 32px;
  }
  .contact-icon {
    width: 20px;
    height: 20px;
    flex: none;
  }
  .edge-bands {
    position: absolute;
    left: 0;
    bottom: 0;
    width: 900px;
    height: 580px;
  }
</style>
</head>
<body>
<main class="canvas">
  <section class="card" aria-label="Business card for Harbourlight ceramics Ltd">
    <div class="brand-watermark" aria-hidden="true"></div>

    <div class="brand">
      <div class="brand-mark" aria-hidden="true"></div>
      <div class="brand-name">
        <span class="primary">Harbourlight</span>
        <span class="secondary">ceramics Ltd</span>
      </div>
    </div>

    <div class="person">
      <p class="person-name">Colin Ashby-Rhodes</p>
      <p class="person-role">Director</p>
    </div>

    <ul class="contacts">
      <li>
        <svg class="contact-icon" viewBox="0 0 20 20" aria-hidden="true">
          <rect x="5" y="1" width="10" height="18" rx="2" fill="var(--brand-orange)"/>
          <rect x="7" y="4" width="6" height="8" fill="#fff"/>
          <circle cx="10" cy="15.5" r="1.3" fill="#fff"/>
        </svg>
        <span>+44 7700 900 318</span>
      </li>
      <li>
        <svg class="contact-icon" viewBox="0 0 20 20" aria-hidden="true">
          <circle cx="10" cy="10" r="9" fill="var(--brand-orange)"/>
          <text x="10" y="14.5" text-anchor="middle" font-family="Open Sans, sans-serif" font-size="13" font-weight="700" fill="#fff">@</text>
        </svg>
        <span>colin@harbourlightceramics.example</span>
      </li>
      <li>
        <svg class="contact-icon" viewBox="0 0 20 20" aria-hidden="true">
          <circle cx="10" cy="10" r="9" fill="var(--brand-orange)"/>
          <g fill="none" stroke="#fff" stroke-width="1.2">
            <circle cx="10" cy="10" r="6"/>
            <ellipse cx="10" cy="10" rx="2.6" ry="6"/>
            <line x1="4" y1="10" x2="16" y2="10"/>
          </g>
        </svg>
        <span>www.harbourlightceramics.example</span>
      </li>
    </ul>

    <svg class="edge-bands" viewBox="0 0 900 580" aria-hidden="true">
      <path d="M640 544 L668 508 L900 500 L900 536 Z" fill="var(--band-grey)"/>
      <path d="M0 580 L0 552 Q320 548 660 536 L900 528 L900 580 Z" fill="var(--brand-orange)"/>
    </svg>
  </section>
</main>
</body>
</html>
```